Business Card for Lawyer

I'm looking for a business card for my new law firm, based in Ontario, Canada. I would prefer single sided. I am partial (but not limited) to white and blue color wise and like things understated. Also, if you can work in the red QK rating symbol from Presworth-Calloway, that would be a plus.

Target Market(s)

Old people - so it should be easy to read.

Industry/Entity Type

Business

Contact Information for Business Card

See the specs in the word document below. Also, see the design for my website. The card should have a similar look to the site.

Requirements
Must have
• Everything listed in the business card specs. I don't mind having the address set off at the bottom of the card on its own line.
Should not have
• 1) Any sort of design that could also be used by a tattoo parlour or a tarot card reader, mystic etc.
• 2) There should not be any photographs of me (or anyone else).

```html
<!DOCTYPE html>
<html lang="en">
<head>
<meta charset="utf-8">
<title>Harlan's Law Firm – Business Card</title>
<link href="https://fonts.googleapis.com/css2?family=Cinzel:wght@400;500&family=Questrial&display=swap" rel="stylesheet">
<style>
  :root {
    --page-bg: #d7d9dc;
    --card-blue: #0b4a72;
    --card-white: #ffffff;
    --text-white: #f4f7fa;
    --accent-blue: #3b8fcf;
    --title-blue: #4d9ad2;
    --badge-neutral: #e3e6ea;
    --ink-dark: #0d1b26;
  }
  * { margin: 0; padding: 0; box-sizing: border-box; }
  html, body {
    width: 1200px; height: 800px; overflow: hidden;
    background: var(--page-bg);
  }
  .business-card {
    position: absolute; left: 100px; top: 110px;
    width: 1000px; height: 580px;
    background: var(--card-white);
    box-shadow: 0 10px 30px rgba(0,0,0,0.18);
    overflow: hidden;
  }
  .card-band {
    position: absolute; left: 0; top: 0;
    width: 1000px; height: 440px;
    background: var(--card-blue);
  }
  .band-watermark {
    position: absolute; left: 78px; top: 118px;
    width: 330px; height: 320px;
    border-radius: 18px;
    background: rgba(255,255,255,0.035);
  }
  .brand-square {
    position: absolute; left: 34px; top: 37px;
    width: 113px; height: 90px;
    background: var(--card-white);
    border: 5px solid var(--ink-dark);
    border-radius: 4px;
  }
  .firm-name {
    position: absolute; left: 165px; top: 40px;
    font-family: "Cinzel", serif; font-weight: 500;
    font-size: 32px; line-height: 42px; letter-spacing: 5px;
    text-transform: uppercase;
    color: var(--text-white);
  }
  .firm-tagline {
    position: absolute; left: 44px; top: 136px;
    font-family: "Questrial", sans-serif;
    font-size: 21px; letter-spacing: 1.6px;
    color: var(--text-white);
  }
  .person-name {
    position: absolute; left: 40px; top: 238px;
    font-family: "Cinzel", serif; font-weight: 400;
    font-size: 30px; letter-spacing: 1px;
    color: var(--text-white);
    white-space: nowrap;
  }
  .person-degree {
    position: absolute; left: 40px; top: 283px;
    font-family: "Cinzel", serif;
    font-size: 22px; letter-spacing: 2px;
    color: var(--text-white);
  }
  .person-title {
    position: absolute; left: 40px; top: 318px;
    font-family: "Questrial", sans-serif;
    font-size: 34px; letter-spacing: 2.5px;
    color: var(--title-blue);
  }
  .column-divider {
    position: absolute; left: 494px; top: 160px;
    width: 2px; height: 228px;
    background: linear-gradient(to bottom, rgba(255,255,255,0), rgba(255,255,255,0.85) 50%, rgba(255,255,255,0));
  }
  .contact-list { list-style: none; }
  .contact-item {
    position: absolute; left: 548px;
    display: flex; align-items: flex-start;
    font-family: "Questrial", sans-serif;
    font-size: 27px; letter-spacing: 1.4px; line-height: 32px;
    color: var(--text-white);
    white-space: nowrap;
  }
  .contact-icon {
    width: 42px; height: 34px; flex: none;
    margin-right: 16px;
    fill: var(--accent-blue);
  }
  .contact-address { top: 89px; }
  .contact-phone { top: 214px; letter-spacing: 2.5px; }
  .contact-fax { top: 275px; letter-spacing: 2.5px; }
  .contact-email { top: 328px; }
  .contact-web { top: 381px; letter-spacing: 2px; }
  .rating-badge {
    position: absolute; left: 627px; top: 448px;
    width: 330px; height: 94px;
    border-radius: 8px;
    background: var(--badge-neutral);
  }
</style>
</head>
<body>
  <div class="business-card">
    <div class="card-band">
      <div class="band-watermark"></div>

      <div class="brand-square"></div>
      <h1 class="firm-name">Harlan’s<br>Law Firm</h1>
      <p class="firm-tagline">Getting the results that matter</p>

      <h2 class="person-name">HARLAN D. WHITCOMBE</h2>
      <p class="person-degree">( J.D)</p>
      <p class="person-title">Lawyer</p>

      <div class="column-divider"></div>

      <ul class="contact-list">
        <li class="contact-item contact-address">
          <svg class="contact-icon" viewBox="0 0 42 34" aria-hidden="true">
            <path d="M14 1a11 11 0 0 1 11 11c0 8-11 21-11 21S3 20 3 12A11 11 0 0 1 14 1zm0 6a5 5 0 1 0 0 10a5 5 0 0 0 0-10z"/>
          </svg>
          <span>14 Alder Lane East,<br>Ground Floor, Fenwick,<br>ON K0X 2B7</span>
        </li>
        <li class="contact-item contact-phone">
          <svg class="contact-icon" viewBox="0 0 42 34" aria-hidden="true">
            <path d="M8 2l6-1 3 8-4 3c2 5 5 9 9 12l4-3 7 4-1 6c-1 2-4 3-7 2C14 29 6 20 4 10 3 6 5 3 8 2z"/>
          </svg>
          <span>555-210-4471</span>
        </li>
        <li class="contact-item contact-fax">
          <svg class="contact-icon" viewBox="0 0 42 34" aria-hidden="true">
            <rect x="1" y="10" width="9" height="23" rx="2"/>
            <path d="M12 12h28v21H12z"/>
            <path d="M17 1h18v9H17z" fill="#0b4a72" stroke="#3b8fcf" stroke-width="2"/>
            <g fill="#0b4a72">
              <rect x="17" y="17" width="17" height="4"/>
              <rect x="17" y="24" width="3" height="3"/><rect x="23" y="24" width="3" height="3"/><rect x="29" y="24" width="3" height="3"/>
              <rect x="17" y="28" width="3" height="3"/><rect x="23" y="28" width="3" height="3"/><rect x="29" y="28" width="3" height="3"/>
            </g>
          </svg>
          <span>555.210.4472</span>
        </li>
        <li class="contact-item contact-email">
          <svg class="contact-icon" viewBox="0 0 42 34" aria-hidden="true">
            <path d="M2 6h38v24H2z"/>
            <path d="M2 6l19 15L40 6M2 30l14-12M40 30L26 18" fill="none" stroke="#0b4a72" stroke-width="2"/>
          </svg>
          <span>harlan@harlansfirm.ca</span>
        </li>
        <li class="contact-item contact-web">
          <svg class="contact-icon" viewBox="0 0 42 34" aria-hidden="true">
            <path d="M2 2h38v24H2z"/>
            <rect x="5" y="5" width="32" height="17" fill="#0b4a72"/>
            <path d="M17 26h8v4h5v3H12v-3h5z"/>
          </svg>
          <span>www.harlansfirm.ca</span>
        </li>
      </ul>
    </div>

    <div class="rating-badge" role="img" aria-label="Presworth-Calloway QK peer rating badge"></div>
  </div>
</body>
</html>
```